Business card for STEADYWAVE

Please design professional business card for IT consulting firm STEADYWAVE INC.
Use logo attached.
Use information from sample qNode business card attached.
replace qnode inc with STEADYWAVE INC.
as well as qnodeinc.com with steadywave.example

```html
<!DOCTYPE html>
<html lang="en">
<head>
<meta charset="utf-8">
<title>STEADYWAVE Business Card</title>
<link href="https://fonts.googleapis.com/css2?family=Montserrat:wght@400;500;700;800&display=swap" rel="stylesheet">
<style>
  :root {
    --bg: #2a2a2c;
    --card-white: #ffffff;
    --card-dark: #1d1d1f;
    --panel-dark: #262628;
    --ink: #1c1c1c;
    --purple: #8a44a3;
    --orange: #f7941d;
    --blue: #5ccbef;
    --green: #6fcbad;
    --grey-text: #2b2b2b;
  }
  * { margin: 0; padding: 0; box-sizing: border-box; }
  html, body {
    width: 1200px; height: 900px; overflow: hidden;
    background: var(--bg);
    font-family: "Montserrat", sans-serif;
  }
  .canvas {
    position: relative; width: 1200px; height: 900px;
  }
  .card {
    position: absolute; left: 250px; width: 700px; height: 400px;
    border-radius: 22px; overflow: hidden;
  }
  .card--front { top: 40px; background: var(--card-white); }
  .card--back { top: 460px; background: var(--card-dark); }

  .edge-stripe {
    position: absolute; left: 0; right: 0; bottom: 0; height: 10px;
    display: flex;
  }
  .edge-stripe span { flex: 1; }
  .edge-stripe .s-orange { background: var(--orange); }
  .edge-stripe .s-blue { background: var(--blue); }
  .edge-stripe .s-purple { background: var(--purple); }
  .edge-stripe .s-green { background: var(--green); }

  /* Front */
  .name-tab {
    position: absolute; left: 0; top: 58px; width: 40px; height: 56px;
    background: var(--purple);
  }
  .person {
    position: absolute; left: 58px; top: 56px;
  }
  .person__name {
    color: var(--purple); font-weight: 800; font-size: 22px;
    letter-spacing: 0.5px; line-height: 1.12;
  }
  .person__role {
    margin-top: 6px; color: var(--grey-text); font-weight: 400;
    font-size: 15px; letter-spacing: 1px;
  }
  .wordmark {
    position: absolute; display: flex; align-items: center; gap: 10px;
    font-weight: 700; letter-spacing: 5px;
  }
  .card--front .wordmark {
    left: 330px; top: 150px; font-size: 36px; color: var(--ink);
  }
  .wordmark__square {
    width: 18px; height: 18px; background: var(--purple);
  }
  .contact {
    position: absolute; left: 330px; top: 215px;
    font-size: 14px; color: var(--grey-text); line-height: 1.55;
  }
  .contact__company {
    color: var(--green); font-weight: 700; font-size: 13px; letter-spacing: 1px;
  }
  .contact__row { display: flex; align-items: center; gap: 8px; }
  .contact__row svg { width: 13px; height: 13px; flex: none; }

  /* Back */
  .back-panel { position: absolute; background: var(--panel-dark); }
  .back-panel--a { left: 0; top: 0; width: 260px; height: 150px; }
  .back-panel--b { left: 380px; top: 0; width: 320px; height: 120px; }
  .back-panel--c { left: 120px; top: 250px; width: 300px; height: 150px; }
  .card--back .wordmark {
    left: 0; right: 0; top: 160px; justify-content: center;
    font-size: 52px; color: #ffffff;
  }
  .card--back .wordmark__square { width: 24px; height: 24px; }
</style>
</head>
<body>
<main class="canvas">
  <section class="card card--front" aria-label="Card front">
    <div class="name-tab"></div>
    <div class="person">
      <p class="person__name">MARKUS VELLAND,<br>P. ENG.</p>
      <p class="person__role">GENERAL MANAGER</p>
    </div>

    <div class="wordmark"><span>STEADYWAVE</span><span class="wordmark__square"></span></div>

    <div class="contact">
      <p class="contact__company">STEADYWAVE INC.</p>
      <p>1200 Harbour Lane, Suite 204</p>
      <p>Oakridge, Ontario, A1B 2C3, Canada</p>
      <p class="contact__row">
        <svg viewBox="0 0 12 12"><rect x="3" y="0.5" width="6" height="11" rx="1" fill="none" stroke="#f7941d" stroke-width="1.2"/><circle cx="6" cy="9.5" r="0.7" fill="#f7941d"/></svg>
        (555) 010-2233
      </p>
      <p class="contact__row">
        <svg viewBox="0 0 12 12"><path d="M2.5 1 L4.5 1 L5.3 3.6 L4 4.6 Q5 7 7.4 8 L8.4 6.7 L11 7.5 L11 9.5 Q10.5 11 9 11 Q1 10 1 3 Q1 1.5 2.5 1 Z" fill="#f7941d"/></svg>
        (555) 010-4455 ext.201
      </p>
      <p class="contact__row">
        <svg viewBox="0 0 12 12"><rect x="0.5" y="2" width="11" height="8" fill="#f7941d"/><path d="M0.5 2 L6 6.5 L11.5 2" fill="none" stroke="#fff" stroke-width="1"/></svg>
        mvelland@steadywave.example
      </p>
      <p class="contact__row">
        <svg viewBox="0 0 12 12"><circle cx="6" cy="6" r="5.3" fill="#f7941d"/><path d="M0.7 6 H11.3 M6 0.7 Q3 6 6 11.3 M6 0.7 Q9 6 6 11.3" fill="none" stroke="#fff" stroke-width="0.8"/></svg>
        www.steadywave.example
      </p>
    </div>

    <div class="edge-stripe"><span class="s-orange"></span><span class="s-blue"></span><span class="s-purple"></span><span class="s-green"></span></div>
  </section>

  <section class="card card--back" aria-label="Card back">
    <div class="back-panel back-panel--a"></div>
    <div class="back-panel back-panel--b"></div>
    <div class="back-panel back-panel--c"></div>
    <div class="wordmark"><span>STEADYWAVE</span><span class="wordmark__square"></span></div>
    <div class="edge-stripe"><span class="s-orange"></span><span class="s-blue"></span><span class="s-purple"></span><span class="s-green"></span></div>
  </section>
</main>
</body>
</html>
```